Help! We need PROFESSIONAL E-mail Signatures that POP!

9/12 UPDATE:
We have extended the deadline.
Also the logo we want used for BelmarTek has changed.

We have 8 employees working for three companies. We want our e-mail signatures to be the same format and cohesive, but each person has one company of the three that needs to be highlighted.
- Logos are attached and spreadsheet shows what information is needed for each employee as well as which of the logos should be the primary logo - first one displayed and slightly larger than the others.
- Please create one design first using the information for Nathaniel Dusset from Line 2 of the spreadsheet (provided three versions - Numbers, Excel, PDF
- All components need to be able to be changed or deleted.
- We need to be able to easily create new signatures for new employees
Updates

Need extra days to review

If you submitted a design prior to yesterday afternoon, please see original brief for the updated BelmarTek logo. This is the version of the BelmarTek logo that will be used for all the email signatures. The spreadsheet with the info for all 8 employees show different versions of this logo for different employees. Ignore that. Use this one logo in the design along with the Velk and Plain logos as indicated on the spreadsheet. Thanks!

Target Market(s)

New/existing clients!

Industry/Entity Type

Property development, commercial construction, property management

Font styles to use
Sans Serif

Requirements
Must have
• A lot of info with a clean look
Nice to have
• Consistency and cohesion
Should not have
• Too many elements - UPDATE: No photos - thanks!

```html
<!DOCTYPE html>
<html lang="en">
<head>
<meta charset="utf-8">
<title>Email Signature - Mockup 3</title>
<link href="https://fonts.googleapis.com/css2?family=Fira+Sans:wght@300;400;500;600;700&display=swap" rel="stylesheet">
<style>
  :root {
    --ink: #333333;
    --ink-soft: #4a4a4a;
    --muted: #6b6b6b;
    --rule: #b9b9b9;
    --brand-green: #66d13a;
    --velk-grey: #3f3f3f;
    --plain-blue: #1d7fc4;
    --card: #ffffff;
  }
  * { box-sizing: border-box; margin: 0; padding: 0; }
  html, body { width: 1200px; height: 1200px; overflow: hidden; }
  body {
    font-family: "Fira Sans", sans-serif;
    color: var(--ink);
    background: linear-gradient(135deg, #fbe9f1 0%, #fdfbee 30%, #fdfcf0 50%, #e1e5f3 72%, #fbe9e4 100%);
    position: relative;
  }
  .page-title {
    position: absolute; top: 272px; left: 0; width: 1200px;
    text-align: center; font-size: 49px; font-weight: 600;
    color: var(--ink-soft); letter-spacing: 0.5px;
  }
  .signature {
    position: absolute; left: 112px; top: 400px; width: 976px; height: 400px;
    background: var(--card);
    box-shadow: 0 2px 8px rgba(0,0,0,0.22);
  }
  .signature > * { position: absolute; }

  .primary-brand { left: 21px; top: 28px; width: 120px; height: 236px; }
  .primary-brand .brand-square {
    position: absolute; left: 0; top: 0; width: 120px; height: 120px;
    background: var(--brand-green);
  }
  .primary-brand .brand-name {
    position: absolute; left: 0; top: 178px; width: 120px;
    font-size: 25px; font-weight: 600; color: var(--ink); text-align: center;
  }

  .person-name { left: 168px; top: 22px; font-size: 30px; font-weight: 600; color: var(--ink); }
  .person-role { left: 168px; top: 58px; font-size: 13.5px; font-weight: 500; color: var(--muted); }

  .license-band {
    left: 164px; top: 88px; width: 271px; height: 46px;
    background: var(--brand-green); color: #fff;
    font-size: 13px; font-weight: 600; line-height: 17px; padding: 6px 9px;
  }

  .partner { top: 152px; font-size: 42px; font-weight: 700; line-height: 1; }
  .partner-velk { left: 168px; color: var(--velk-grey); }
  .partner-plain { left: 345px; color: var(--plain-blue); }

  .contact-label { font-size: 15.5px; font-weight: 600; color: #111; }
  .contact-value { font-size: 13.5px; font-weight: 400; color: var(--ink-soft); }
  .phone-label { left: 473px; top: 54px; }
  .phone-value { left: 473px; top: 72px; }
  .address-label { left: 604px; top: 54px; }
  .address-value { left: 604px; top: 72px; }

  .rule { height: 1px; background: var(--rule); }
  .rule-top { left: 473px; top: 98px; width: 478px; }
  .rule-mid { left: 473px; top: 195px; width: 478px; }
  .rule-full { left: 19px; top: 262px; width: 932px; }

  .contact-line { left: 473px; font-size: 16px; color: var(--ink-soft); }
  .contact-line strong { font-weight: 600; color: #111; }
  .line-office { top: 113px; }
  .line-email { top: 138px; }
  .line-web { top: 162px; }

  .notice-title { left: 19px; top: 278px; font-size: 15.5px; font-weight: 600; color: #111; }
  .notice-body {
    left: 19px; top: 302px; width: 932px;
    font-size: 13.6px; font-weight: 300; line-height: 17.4px;
    color: var(--ink-soft); text-align: justify;
  }
</style>
</head>
<body>
  <h1 class="page-title">Email Signature- Mockup 3</h1>

  <section class="signature">
    <div class="primary-brand">
      <div class="brand-square"></div>
      <div class="brand-name">BelmarTek</div>
    </div>

    <h2 class="person-name">Nathaniel Dusset</h2>
    <p class="person-role">CEO/Owner</p>

    <div class="license-band">
      IL RE Lic#: 475.019832<br>
      Chicago GC Lic #: TGC041185
    </div>

    <div class="partner partner-velk">Velk</div>
    <div class="partner partner-plain">Plain</div>

    <div class="contact-label phone-label">Phone</div>
    <div class="contact-value phone-value">312-555-0148(D)</div>
    <div class="contact-label address-label">Address</div>
    <div class="contact-value address-value">120 N. Maple Ave., Ste 4B, Lakeview IL 60600</div>

    <div class="rule rule-top"></div>
    <p class="contact-line line-office"><strong>BelmarTek:</strong> 312-555-0190 <strong>x 101</strong></p>
    <p class="contact-line line-email"><strong>E:</strong>&nbsp; ndusset@belmartek.com</p>
    <p class="contact-line line-web"><strong>W:</strong> www.belmartek.com</p>
    <div class="rule rule-mid"></div>

    <div class="rule rule-full"></div>
    <h3 class="notice-title">CONFIDENTIALITY NOTICE:</h3>
    <p class="notice-body">This e-mail is intended only for the recipient named and may contain confidential, privileged, and exempt from disclosure under applicable laws. If you are not the named recipient, you may have received this transmission in error. We ask that you, please immediately notify us by e-mail at operations@belmartek.com and remove this and all attached file(s) from your system. You are notified that any disclosure, copying, distribution, or use of the information in this transmission if you are not the intended recipient is prohibited and may expose you to liability.</p>
  </section>
</body>
</html>
```